11 x 11 Flyer Design for Social Media - Reverse Mortgages

62 or older?

A Reverse Mortgage
could be
Your Road to Financial Freedom

* No Monthly Payments
* No Income Requirements
* No Credit Score Requirements
* No Loss of Ownership

Receive cash by lump sum, monthly installments or a line of credit!!

Call us today for a Free Consultation!!
(800) 471-2965

Bluegate Financial Services, Inc.
NMLS #318760
www.bluegatehome.com

```html
<!DOCTYPE html>
<html lang="en">
<head>
<meta charset="utf-8">
<title>Reverse Mortgage Flyer – Bluegate Financial Services</title>
<link rel="stylesheet" href="https://fonts.googleapis.com/css2?family=Montserrat:wght@300;400;500;700;800&display=swap">
<style>
  :root {
    --navy-deep: #162a5c;
    --navy: #20408a;
    --navy-mid: #2a4c98;
    --ink: #1f3f86;
    --white: #ffffff;
    --soft-white: #e9eef8;
    --photo-warm: #b99a7c;
    --photo-sky: #a8c4d8;
  }
  * { margin: 0; padding: 0; box-sizing: border-box; }
  html, body { width: 1200px; height: 1200px; overflow: hidden; }
  body {
    font-family: "Montserrat", Arial, sans-serif;
    background: var(--navy-deep);
  }
  .flyer {
    position: relative;
    width: 1200px;
    height: 1200px;
    overflow: hidden;
    color: var(--white);
    background: linear-gradient(160deg, var(--navy-mid) 0%, var(--navy) 45%, var(--navy-deep) 100%);
  }
  .age-tag {
    position: absolute;
    left: 0;
    top: 103px;
    width: 720px;
    height: 152px;
    background: var(--white);
    border-radius: 0 30px 30px 0;
    display: flex;
    align-items: center;
    padding-left: 40px;
  }
  .age-tag h1 {
    color: var(--ink);
    font-size: 96px;
    font-weight: 700;
    letter-spacing: -2px;
    line-height: 1;
  }
  .couple-photo {
    position: absolute;
    left: 828px;
    top: -82px;
    width: 480px;
    height: 480px;
    border-radius: 50%;
    border: 10px solid var(--white);
    background: radial-gradient(circle at 40% 60%, var(--photo-warm) 0%, #8a6f5a 40%, var(--photo-sky) 100%);
    box-shadow: 0 0 0 8px rgba(120,160,220,0.35);
  }
  .headline {
    position: absolute;
    left: 30px;
    top: 338px;
    font-size: 50px;
    font-weight: 700;
    line-height: 68px;
  }
  .payout-options {
    position: absolute;
    left: 30px;
    top: 484px;
    font-size: 41px;
    font-weight: 300;
    line-height: 58px;
    color: var(--soft-white);
  }
  .benefits {
    position: absolute;
    left: 30px;
    top: 656px;
    list-style: none;
  }
  .benefits li {
    display: flex;
    align-items: center;
    height: 61px;
    font-size: 35px;
    font-weight: 400;
  }
  .benefits svg { width: 30px; height: 30px; margin-right: 24px; flex: none; }
  .call-box {
    position: absolute;
    right: 0;
    top: 682px;
    width: 529px;
    height: 148px;
    background: var(--white);
    border-radius: 30px 0 0 30px;
    color: var(--ink);
    display: flex;
    flex-direction: column;
    align-items: center;
    justify-content: center;
  }
  .call-box .invite { font-size: 27px; font-weight: 400; }
  .call-box .phone { font-size: 42px; font-weight: 700; margin-top: 6px; }
  .company {
    position: absolute;
    left: 30px;
    bottom: 72px;
  }
  .company .name { font-size: 33px; font-weight: 700; }
  .company .license { font-size: 27px; font-weight: 300; margin-top: 12px; }
  .website {
    position: absolute;
    right: 20px;
    bottom: 34px;
    font-size: 26px;
    font-weight: 500;
  }
</style>
</head>
<body>
<main class="flyer">
  <div class="age-tag"><h1>62 or older?</h1></div>

  <div class="couple-photo" role="img" aria-label="Photo of a smiling senior couple riding in a convertible car"></div>

  <h2 class="headline">A Reverse Mortgage could be<br>Your Road to Financial Freedom</h2>

  <p class="payout-options">Receive cash by lump sum,<br>monthly installments or a line of credit!!</p>

  <ul class="benefits">
    <li><svg viewBox="0 0 30 30" aria-hidden="true"><circle cx="15" cy="15" r="14" fill="#fff"/><path d="M8.5 15.5l4.5 4.5 8.5-9" fill="none" stroke="#20408a" stroke-width="3.4" stroke-linecap="round" stroke-linejoin="round"/></svg>No Monthly Payments</li>
    <li><svg viewBox="0 0 30 30" aria-hidden="true"><circle cx="15" cy="15" r="14" fill="#fff"/><path d="M8.5 15.5l4.5 4.5 8.5-9" fill="none" stroke="#20408a" stroke-width="3.4" stroke-linecap="round" stroke-linejoin="round"/></svg>No Income Requirements</li>
    <li><svg viewBox="0 0 30 30" aria-hidden="true"><circle cx="15" cy="15" r="14" fill="#fff"/><path d="M8.5 15.5l4.5 4.5 8.5-9" fill="none" stroke="#20408a" stroke-width="3.4" stroke-linecap="round" stroke-linejoin="round"/></svg>No Credit Score Requirements</li>
    <li><svg viewBox="0 0 30 30" aria-hidden="true"><circle cx="15" cy="15" r="14" fill="#fff"/><path d="M8.5 15.5l4.5 4.5 8.5-9" fill="none" stroke="#20408a" stroke-width="3.4" stroke-linecap="round" stroke-linejoin="round"/></svg>No Loss of Ownership</li>
  </ul>

  <div class="call-box">
    <p class="invite">Call us today for a Free Consultation!!</p>
    <p class="phone">(800) 471-2965</p>
  </div>

  <div class="company">
    <p class="name">Bluegate Financial Services, Inc.</p>
    <p class="license">NMLS #318760</p>
  </div>

  <p class="website">www.bluegatehome.com</p>
</main>
</body>
</html>
```